Business Cards for our company

Hi there,

we have successfully designed a logo with ArtFlock and would like now to design our business cards. We would like to keep the colours and the look-and-feel of the logo. Please send in variations with two or three colours and one or two sides. I promise to respond to every single submission.

Many thanks and happy new year.

All the best,
Wilfried

Target Market(s)

B2B

Industry/Entity Type

Trade

Contact Information for Business Card

We have successfully designed a logo with ArtFlock and would like now to design our business cards. We would like to keep the colours and the look-and-feel of the logo. Please send in variations with two or three colours and one or two sides. I promise to respond to every single submission.

Font styles to use
Serif
Sans Serif
Script

Requirements
Must have
• These information should be on the business card, grouped as you suggest, and we think using small pictograms for mobile, email, etc is pretty helpful:
• Wilfried Tammler (first and second name)
• Geschäftsführer/ Managing Director (title)
• KoR Warenkontor GmbH (company name and legal form)
• Ostheimer Str. 18/3 (street and house number)
• 70839 Gerlingen (zip code and town)
• +491709384562 (mobile)
• +4971569027341 (work)
• w.tammler@kor-warenkontor.example (email)
• www.kor-warenkontor.example (web)
Nice to have
• Spectacular and interesting layout and design. You look at it and think, wow, that's not the normal stuff.
• We think of ourselves as bridge-builders between businesses (international producers on the one hand, and retail chains on the other hand) and we translate, organise and manage projects where both partners are involved, but it's difficult for them to cooperate due to language barriers and different working cultures.
• This is why we have the n between the B's shaped as a bridge, and the green arc supports this idea. Maybe you could play with this idea...
Should not have
• the standard layout that everybody has

```html
<!DOCTYPE html>
<html lang="de">
<head>
<meta charset="utf-8">
<title>KoR Warenkontor – Visitenkarten</title>
<link href="https://fonts.googleapis.com/css2?family=Montserrat:wght@400;500;600;700;800&display=swap" rel="stylesheet">
<style>
  :root {
    --backdrop: #9cc92c;
    --ink: #1b1b1b;
    --teal: #1d5a6a;
    --teal-mid: #23786e;
    --green-deep: #05973f;
    --front-letter: rgba(190, 215, 215, 0.55);
    --mint-pale: #e3f0ec;
    --white: #ffffff;
  }
  * { box-sizing: border-box; margin: 0; padding: 0; }
  html, body { width: 1200px; height: 1200px; overflow: hidden; }
  body {
    background: var(--backdrop);
    font-family: "Montserrat", sans-serif;
    position: relative;
  }
  .card {
    position: absolute;
    width: 293px;
    height: 502px;
    overflow: hidden;
  }
  .card--front-portrait { left: 238px; top: 190px; }
  .card--back-portrait { left: 666px; top: 190px; }
  .card-landscape {
    position: absolute;
    width: 502px;
    height: 292px;
    overflow: hidden;
  }
  .card-landscape--front { left: 84px; top: 808px; }
  .card-landscape--back { left: 630px; top: 808px; }
  .card-landscape .card { left: 104px; top: -105px; }
  .card-landscape--front .card { transform: rotate(-90deg); }
  .card-landscape--back .card { transform: rotate(90deg); }

  /* background facets, kept as soft fills */
  .facets { position: absolute; inset: 0; }

  /* giant decorative letters */
  .giant {
    position: absolute;
    left: 0;
    right: 0;
    font-weight: 800;
    line-height: 0.8;
    text-align: center;
    pointer-events: none;
  }
  .giant--upper { top: 222px; font-size: 250px; }
  .giant--lower { top: 418px; font-size: 250px; }
  .front .giant { color: var(--front-letter); }
  .back .giant { color: var(--green-deep); }
  .back .giant--lower { opacity: 0.55; }

  /* front */
  .front {
    background: linear-gradient(180deg, var(--mint-pale) 0%, #f1f6ef 45%, #e6f0d2 80%, #d9e9b8 100%);
  }
  .front .facets {
    background:
      linear-gradient(120deg, transparent 0 55%, rgba(200,225,160,0.35) 55% 100%),
      linear-gradient(60deg, rgba(220,236,230,0.5) 0 40%, transparent 40% 100%);
  }
  .wordmark {
    position: absolute;
    left: 22px;
    top: 20px;
    color: var(--ink);
    font-weight: 800;
    line-height: 1;
  }
  .wordmark__short { display: block; font-size: 104px; letter-spacing: -2px; }
  .wordmark__long { display: block; font-size: 27px; letter-spacing: 1.5px; margin-top: 10px; }

  /* back */
  .back {
    background: linear-gradient(180deg, var(--teal) 0%, var(--teal-mid) 25%, #3aa25a 45%, #6cbc4c 70%, #c9e09a 100%);
    color: var(--white);
    text-align: center;
  }
  .back .facets {
    background:
      linear-gradient(120deg, transparent 0 50%, rgba(255,255,255,0.08) 50% 100%),
      linear-gradient(60deg, rgba(0,60,60,0.12) 0 35%, transparent 35% 100%);
  }
  .name-band {
    position: relative;
    background: var(--white);
    margin-top: 18px;
    padding: 4px 0 5px;
  }
  .name-band__name {
    color: var(--teal);
    font-weight: 800;
    font-size: 18.5px;
    letter-spacing: 1.3px;
    line-height: 1.15;
  }
  .name-band__title { color: var(--teal); font-size: 10.5px; line-height: 1.2; }
  .contact {
    position: relative;
    margin-top: 10px;
    font-weight: 500;
    font-size: 12px;
    line-height: 16.5px;
    letter-spacing: 0.3px;
    text-transform: uppercase;
  }
  .contact__company { font-size: 13px; margin-bottom: 7px; }
  .contact__row { display: flex; justify-content: center; align-items: center; gap: 4px; white-space: nowrap; }
  .contact__row--small { font-size: 10.6px; letter-spacing: 0; }
  .icon { width: 11px; height: 11px; flex: none; }
</style>
</head>
<body>
<svg width="0" height="0" style="position:absolute" aria-hidden="true">
  <defs>
    <symbol id="i-mobile" viewBox="0 0 12 12"><circle cx="6" cy="6" r="6" fill="#fff"/><rect x="4" y="2.5" width="4" height="7" rx="0.8" fill="#1d5a6a"/></symbol>
    <symbol id="i-phone" viewBox="0 0 12 12"><circle cx="6" cy="6" r="6" fill="#fff"/><path d="M4 3.2l1.3 1.6-.7.8c.4.9 1 1.5 1.8 1.9l.8-.7 1.6 1.3-.8 1C6.1 8.9 3.4 6.3 3.2 4z" fill="#1d5a6a"/></symbol>
    <symbol id="i-mail" viewBox="0 0 12 12"><circle cx="6" cy="6" r="6" fill="#fff"/><rect x="3" y="4" width="6" height="4.2" fill="#1d5a6a"/><path d="M3 4l3 2.3L9 4" stroke="#fff" stroke-width="0.7" fill="none"/></symbol>
    <symbol id="i-pin" viewBox="0 0 12 12"><circle cx="6" cy="6" r="6" fill="#fff"/><path d="M6 2.5a2.3 2.3 0 0 1 2.3 2.3C8.3 6.5 6 9.5 6 9.5S3.7 6.5 3.7 4.8A2.3 2.3 0 0 1 6 2.5z" fill="#1d5a6a"/><circle cx="6" cy="4.8" r="0.9" fill="#fff"/></symbol>
    <symbol id="i-web" viewBox="0 0 12 12"><circle cx="6" cy="6" r="6" fill="#fff"/><circle cx="6" cy="6" r="3.3" fill="none" stroke="#1d5a6a" stroke-width="0.8"/><path d="M2.7 6h6.6M6 2.7v6.6" stroke="#1d5a6a" stroke-width="0.8"/></symbol>
  </defs>
</svg>

<!-- portrait front -->
<section class="card card--front-portrait front">
  <div class="facets" role="img" aria-label="Soft faceted triangle pattern in pale mint and lime"></div>
  <div class="giant giant--upper" aria-hidden="true">K</div>
  <div class="giant giant--lower" aria-hidden="true">o</div>
  <div class="wordmark"><span class="wordmark__short">KoR</span><span class="wordmark__long">WARENKONTOR</span></div>
</section>

<!-- portrait back -->
<section class="card card--back-portrait back">
  <div class="facets" role="img" aria-label="Faceted triangle pattern in teal and green"></div>
  <div class="giant giant--upper" aria-hidden="true">R</div>
  <div class="giant giant--lower" aria-hidden="true">o</div>
  <div class="name-band">
    <div class="name-band__name">WILFRIED TAMMLER</div>
    <div class="name-band__title">Geschäftsführer/ Managing Director</div>
  </div>
  <div class="contact">
    <div class="contact__company">KOR WARENKONTOR GMBH</div>
    <div class="contact__row"><svg class="icon"><use href="#i-mobile"/></svg>+491709384562 | <svg class="icon"><use href="#i-phone"/></svg>+4971569027341</div>
    <div class="contact__row contact__row--small"><svg class="icon"><use href="#i-mail"/></svg>W.TAMMLER@KOR-WARENKONTOR.EXAMPLE</div>
    <div class="contact__row"><svg class="icon"><use href="#i-pin"/></svg>OSTHEIMER STR. 18/3</div>
    <div class="contact__row">70839 GERLINGEN</div>
    <div class="contact__row contact__row--small"><svg class="icon"><use href="#i-web"/></svg>WWW.KOR-WARENKONTOR.EXAMPLE</div>
  </div>
</section>

<!-- landscape front -->
<div class="card-landscape card-landscape--front">
  <section class="card front">
    <div class="facets" role="img" aria-label="Soft faceted triangle pattern in pale mint and lime"></div>
    <div class="giant giant--upper" aria-hidden="true">K</div>
    <div class="giant giant--lower" aria-hidden="true">o</div>
    <div class="wordmark"><span class="wordmark__short">KoR</span><span class="wordmark__long">WARENKONTOR</span></div>
  </section>
</div>

<!-- landscape back -->
<div class="card-landscape card-landscape--back">
  <section class="card back">
    <div class="facets" role="img" aria-label="Faceted triangle pattern in teal and green"></div>
    <div class="giant giant--upper" aria-hidden="true">R</div>
    <div class="giant giant--lower" aria-hidden="true">o</div>
    <div class="name-band">
      <div class="name-band__name">WILFRIED TAMMLER</div>
      <div class="name-band__title">Geschäftsführer/ Managing Director</div>
    </div>
    <div class="contact">
      <div class="contact__company">KOR WARENKONTOR GMBH</div>
      <div class="contact__row"><svg class="icon"><use href="#i-mobile"/></svg>+491709384562 | <svg class="icon"><use href="#i-phone"/></svg>+4971569027341</div>
      <div class="contact__row contact__row--small"><svg class="icon"><use href="#i-mail"/></svg>W.TAMMLER@KOR-WARENKONTOR.EXAMPLE</div>
      <div class="contact__row"><svg class="icon"><use href="#i-pin"/></svg>OSTHEIMER STR. 18/3</div>
      <div class="contact__row">70839 GERLINGEN</div>
      <div class="contact__row contact__row--small"><svg class="icon"><use href="#i-web"/></svg>WWW.KOR-WARENKONTOR.EXAMPLE</div>
    </div>
  </section>
</div>
</body>
</html>
```